Launching a new real estate agency in Monaco

Hello, I am opening a new real estate agency in Monaco. For the purpose of my activity, in order to be known quickly among a fierce competition I need an advertising campaign that will be broadcast in local magazines, newspapers, paper board, etc.

You will find example of pictures of Monaco on which I have the rights and my logo. You can always pick other images that I can buy if the price is reasonable for a commercial use (<200 $)

Please respect the color code.

I wish you good luck and look forward to give you my feedbacks

Reason: Only few projects posted were respecting the brief and of quality. Hoping to receive more in coming days

Target Market(s)

International high-end clientele of all ages, all genders.

Industry/Entity Type

Real Estate Agent

Font styles to use
Serif

Requirements
Must have
• 1/ My logo
• 2/ This message "Un nouveau regard sur l'immobilier" means in English a fresh look at real estate or new eyes on real-estate.
• 3/ My address: 14 rue des Orvilles, Passage Marcellin, 98 000 Monaco
• 4/ Phone number: +377.93.48.25.71
• 5/ Website: www.brunor-agency.com.
• 6/ Format: Files should be easily adjustable but I'd like a vertical display to fit easily in Magazines, Poster and billboard. So please work in high resolution !
Nice to have
• Please think about your design in accordance with the message I want to display.
Should not have
• A simple poster with a picture of Monaco that does not take into consideration the message of the advertisement, "Un nouveau regard sur l'immobilier" which means in english, new eyes on real-estate or a new look at real-estate, or new vision at real-estate.

```html
<!DOCTYPE html>
<html lang="fr">
<head>
<meta charset="utf-8">
<title>Brunor Agency – Un nouveau regard sur l'immobilier</title>
<link rel="stylesheet" href="https://fonts.googleapis.com/css2?family=Nunito:wght@800;900&family=Rajdhani:wght@600;700&display=swap">
<style>
  :root {
    --page: #ffffff;
    --aqua: #b8eaec;
    --navy: #1c2a40;
    --copper-dark: #c4856f;
    --copper-light: #f3c6b6;
    --window: #fbfbfb;
    --ink: #1e2738;
    --dot-red: #f07a86;
    --dot-green: #7fd07f;
    --dot-yellow: #f3f07a;
  }
  * { margin: 0; padding: 0; box-sizing: border-box; }
  html, body {
    width: 1200px; height: 1170px; overflow: hidden;
    background: var(--page);
  }
  .poster {
    position: absolute; left: 277px; top: 130px;
    width: 646px; height: 910px;
    background: var(--aqua);
    overflow: hidden;
    font-family: "Nunito", sans-serif;
  }
  .brand-panel {
    position: absolute; left: 227px; top: 0;
    width: 419px; height: 155px;
    background: var(--navy);
    border-bottom-left-radius: 58px;
    display: flex; align-items: center; justify-content: center; gap: 16px;
    padding-left: 10px;
  }
  .brand-mark {
    width: 42px; height: 42px; flex: none;
    background: linear-gradient(135deg, var(--copper-dark), var(--copper-light));
  }
  .brand-name {
    font-family: "Rajdhani", sans-serif; font-weight: 700;
    font-size: 34px; letter-spacing: 3px; line-height: 1;
    color: var(--copper-light);
    white-space: nowrap;
  }
  .browser {
    position: absolute; left: 51px; top: 216px;
    width: 560px; height: 386px;
    background: var(--window);
  }
  .browser-tail { position: absolute; left: 115px; top: 601px; }
  .browser-nav { position: absolute; left: 15px; top: 20px; }
  .browser-dots { position: absolute; right: 16px; top: 19px; display: flex; gap: 12px; }
  .browser-dots span { width: 21px; height: 21px; border-radius: 50%; }
  .dot-red { background: var(--dot-red); }
  .dot-green { background: var(--dot-green); }
  .dot-yellow { background: var(--dot-yellow); }
  .browser-view {
    position: absolute; left: 15px; top: 50px;
    width: 530px; height: 316px;
    background: linear-gradient(180deg, #e9a35a 0%, #d98ca0 22%, #b98fc7 45%, #8d6f8f 70%, #4a3a3a 100%);
    border: 2px solid #222;
  }
  .search-bar {
    position: absolute; left: 64px; top: 124px;
    width: 411px; height: 38px;
    background: rgba(236, 226, 236, 0.85);
    border: 2px solid #1a1a1a;
    display: flex; align-items: center; justify-content: space-between;
    padding: 0 8px 0 12px;
  }
  .search-text {
    font-weight: 800; font-size: 21px; color: var(--ink);
    white-space: nowrap;
  }
  .address {
    position: absolute; left: 55px; top: 686px; width: 200px;
    text-align: center; font-style: normal;
    font-weight: 800; font-size: 21px; line-height: 25px;
    color: var(--navy);
  }
  .call-band {
    position: absolute; left: 0; top: 848px;
    width: 311px; height: 62px;
    background: linear-gradient(90deg, var(--copper-dark), var(--copper-light) 60%, var(--copper-dark));
    border-top-right-radius: 26px;
    display: flex; align-items: center; justify-content: center;
    font-weight: 800; font-size: 24px; color: #3a2a28;
    white-space: nowrap;
  }
  .web-band {
    position: absolute; left: 311px; top: 867px;
    width: 335px; height: 43px;
    background: var(--navy);
    display: flex; align-items: center; justify-content: center;
    font-weight: 800; font-size: 21px; color: #ffffff;
    white-space: nowrap;
  }
</style>
</head>
<body>
  <main class="poster">
    <header class="brand-panel">
      <div class="brand-mark"></div>
      <div class="brand-name">BRUNOR AGENCY</div>
    </header>

    <section class="browser">
      <svg class="browser-nav" width="70" height="30" viewBox="0 0 70 30" aria-hidden="true">
        <polygon points="0,15 25,3 25,27" fill="#3a3a3a"/>
        <polygon points="32,3 57,15 32,27" fill="#3a3a3a"/>
      </svg>
      <div class="browser-dots">
        <span class="dot-red"></span><span class="dot-green"></span><span class="dot-yellow"></span>
      </div>
      <div class="browser-view" role="img" aria-label="Vue aérienne de Monaco au coucher du soleil, côte et immeubles illuminés">
        <div class="search-bar">
          <span class="search-text">Un nouveau regard sur l'immobilier</span>
          <svg width="24" height="26" viewBox="0 0 24 26" aria-hidden="true">
            <circle cx="10" cy="10" r="8" fill="none" stroke="#1a1a1a" stroke-width="2.5"/>
            <line x1="15" y1="16" x2="22" y2="24" stroke="#1a1a1a" stroke-width="2.5" stroke-linecap="round"/>
          </svg>
        </div>
      </div>
    </section>
    <svg class="browser-tail" width="86" height="65" viewBox="0 0 86 65" aria-hidden="true">
      <polygon points="0,0 86,0 86,65" fill="var(--window)"/>
    </svg>

    <address class="address">14 rue des<br>Orvilles,<br>Passage<br>Marcellin,<br>98 000 Monaco</address>

    <div class="call-band">Call: +377.93.48.25.71</div>
    <div class="web-band">www.brunor-agency.com</div>
  </main>
</body>
</html>
```